New Zealand Marlborough Sauvignon Blanc wine packaging design

We need packaging design for our new wine brand, Halloway Brisk. The wine is a New Zealand Marlborough Sauvignon Blanc. We would like the packaging will portray elegance and style with an understated label. We are looking for a label that portrays the elegance of the French Riviera. The label should be round or pill shaped.

Industry/Entity Type

Wine

Font styles to use
Serif
Sans Serif

Requirements
Must have
• The words in order of importance: Halloway Brisk, Sauvignon Blanc, Marlborough, New Zealand. It should be fit to the bottle posted in the links
Nice to have
• a pill shape or circular shape
Should not have
• Illustrations of wine bottles, wine glasses, or grapes

```html
<!DOCTYPE html>
<html lang="en">
<head>
<meta charset="utf-8">
<title>Halloway Brisk Sauvignon Blanc Label</title>
<link rel="stylesheet" href="https://fonts.googleapis.com/css2?family=Cormorant+Garamond:wght@500;600&family=Great+Vibes&display=swap">
<style>
  :root {
    --bg: #0d0d09;
    --line-outer: #d6de68;
    --line-inner: #e6f05c;
    --ink: #ffffff;
    --scene-top: #f2ee1a;
    --scene-mid: #a9a324;
    --scene-bottom: #5c5a22;
  }
  html, body {
    margin: 0;
    padding: 0;
    width: 1200px;
    height: 1200px;
    overflow: hidden;
    background: var(--bg);
  }
  .label {
    display: block;
    width: 1200px;
    height: 1200px;
  }
  .frame-outer { fill: none; stroke: var(--line-outer); stroke-width: 2; }
  .frame-main { fill: none; stroke: var(--line-inner); stroke-width: 4; }
  .frame-window { fill: none; stroke: var(--line-inner); stroke-width: 2; }
  .brand-arc {
    font-family: "Cormorant Garamond", serif;
    font-weight: 600;
    font-size: 58px;
    letter-spacing: 12px;
    fill: var(--ink);
  }
  .region-arc {
    font-family: "Cormorant Garamond", serif;
    font-weight: 600;
    font-size: 20px;
    letter-spacing: 4px;
    fill: var(--ink);
  }
  .varietal {
    font-family: "Great Vibes", cursive;
    font-size: 72px;
    fill: var(--ink);
  }
</style>
</head>
<body>
<svg class="label" viewBox="0 0 1200 1200" xmlns="http://www.w3.org/2000/svg">
  <defs>
    <linearGradient id="sceneTone" x1="0" y1="0" x2="0" y2="1">
      <stop offset="0" stop-color="var(--scene-top)"/>
      <stop offset="0.5" stop-color="var(--scene-mid)"/>
      <stop offset="1" stop-color="var(--scene-bottom)"/>
    </linearGradient>
    <path id="brandPath" d="M 365 620 L 365 460 A 235 235 0 0 1 835 460 L 835 620"/>
    <path id="regionPath" d="M 335 740 A 265 265 0 0 0 865 740"/>
  </defs>

  <rect class="frame-outer" x="270" y="130" width="660" height="940" rx="330"/>
  <rect class="frame-main" x="292" y="152" width="616" height="896" rx="308"/>

  <rect class="frame-window" x="406" y="278" width="388" height="650" rx="194"/>
  <rect class="scene-window" x="418" y="290" width="364" height="626" rx="182" fill="url(#sceneTone)"
        role="img" aria-label="Watercolour illustration of a Riviera villa on a rocky seaside cliff"/>

  <text class="brand-arc" text-anchor="middle">
    <textPath href="#brandPath" startOffset="50%">HALLOWAY BRISK</textPath>
  </text>

  <text class="varietal" x="600" y="770" text-anchor="middle">Sauvignon</text>
  <text class="varietal" x="600" y="850" text-anchor="middle">Blanc</text>

  <text class="region-arc" text-anchor="middle">
    <textPath href="#regionPath" startOffset="50%">MARLBOROUGH, NEW ZEALAND.</textPath>
  </text>
</svg>
</body>
</html>
```